Simple but elegant business card/logo design for exclusive beauty business

We need a logo designed for a new elegant and exclusive beauty business called "G". The logo itself should be a stylistic and custom design for the letter "G". We would like the business card to have the logo as the centrepiece on a clean background. Gold Logo on black background or silver on white background.

The business card details should be displayed centre of the card. Details are as follows:

Tamsin Rowe
Facebook: /simplyshinebyr
Instagram: /simplyshinebyr

The words "Simply Shine" should also appear somewhere on the card.

G

• Design must be simple, clean and elegant
• The design should not be cluttered

```html
<!DOCTYPE html>
<html lang="en">
<head>
<meta charset="utf-8">
<title>Simply Shine by R — Business Card</title>
<link href="https://fonts.googleapis.com/css2?family=Open+Sans:wght@400;600&display=swap" rel="stylesheet">
<style>
  :root {
    --page: #e4e4e4;
    --card: #ffffff;
    --silver-dark: #6d6d6d;
    --silver: #8f8f8f;
    --silver-light: #b9b9b9;
    --silver-faint: #eeeeee;
    --shadow: rgba(0, 0, 0, 0.18);
  }
  * { box-sizing: border-box; margin: 0; padding: 0; }
  html, body { width: 857px; height: 1200px; overflow: hidden; }
  body {
    background: var(--page);
    font-family: "Open Sans", Arial, sans-serif;
    color: var(--silver);
    position: relative;
  }
  .card {
    position: absolute;
    left: 78px;
    width: 700px;
    height: 400px;
    background: var(--card);
    box-shadow: 0 10px 30px var(--shadow);
    overflow: hidden;
  }
  .card--front { top: 150px; }
  .card--back { top: 650px; }

  /* front: brand centred on a clean field */
  .front__accent {
    position: absolute;
    left: 50%; top: 50%;
    width: 520px; height: 520px;
    transform: translate(-50%, -50%);
    border-radius: 50%;
    background: var(--silver-faint);
  }
  .front__brand {
    position: absolute;
    inset: 0;
    display: flex;
    align-items: center;
    justify-content: center;
    font-size: 40px;
    font-weight: 600;
    color: var(--silver-dark);
    letter-spacing: 0.5px;
  }

  /* back: brand, divider, contact details */
  .back__brand {
    position: absolute;
    left: 60px; top: 130px;
    width: 240px;
    font-size: 34px;
    line-height: 1.15;
    font-weight: 600;
    color: var(--silver-dark);
  }
  .back__divider {
    position: absolute;
    left: 330px; top: 90px;
    width: 1px; height: 220px;
    background: linear-gradient(to bottom, transparent, var(--silver) 20%, var(--silver) 80%, transparent);
  }
  .contact {
    position: absolute;
    left: 370px; top: 110px;
  }
  .contact__name {
    font-size: 24px;
    font-weight: 400;
    color: var(--silver);
    margin-bottom: 16px;
  }
  .contact__list { list-style: none; }
  .contact__item {
    display: flex;
    align-items: center;
    gap: 12px;
    font-size: 15px;
    font-weight: 600;
    color: var(--silver-dark);
    margin-bottom: 8px;
  }
  .contact__icon {
    width: 15px; height: 15px;
    flex: none;
  }
  .contact__icon--square {
    background: var(--silver);
    border-radius: 2px;
  }
</style>
</head>
<body>

<section class="card card--front" aria-label="Card front">
  <div class="front__accent"></div>
  <div class="front__brand">Simply Shine by R</div>
</section>

<section class="card card--back" aria-label="Card back">
  <div class="back__brand">Simply Shine<br>by R</div>
  <div class="back__divider"></div>
  <div class="contact">
    <p class="contact__name">Tamsin Rowe</p>
    <ul class="contact__list">
      <li class="contact__item">
        <svg class="contact__icon" viewBox="0 0 16 16" aria-hidden="true">
          <rect x="4" y="1" width="8" height="14" rx="1.5" fill="none" stroke="#8f8f8f" stroke-width="1.6"/>
          <circle cx="8" cy="12.3" r="0.9" fill="#8f8f8f"/>
        </svg>
        0207 946 0318
      </li>
      <li class="contact__item">
        <svg class="contact__icon" viewBox="0 0 16 16" aria-hidden="true">
          <rect x="1" y="3" width="14" height="10" rx="1" fill="#8f8f8f"/>
          <path d="M1.5 3.8 8 9l6.5-5.2" fill="none" stroke="#fff" stroke-width="1.3"/>
        </svg>
        hello@simplyshinebyr.com
      </li>
      <li class="contact__item">
        <svg class="contact__icon" viewBox="0 0 16 16" aria-hidden="true">
          <circle cx="8" cy="8" r="6.5" fill="none" stroke="#8f8f8f" stroke-width="1.4"/>
          <ellipse cx="8" cy="8" rx="2.8" ry="6.5" fill="none" stroke="#8f8f8f" stroke-width="1.1"/>
          <path d="M1.5 8h13" stroke="#8f8f8f" stroke-width="1.1"/>
        </svg>
        www.simplyshinebyr.com
      </li>
      <li class="contact__item">
        <span class="contact__icon contact__icon--square"></span>
        /simplyshinebyr
      </li>
      <li class="contact__item">
        <span class="contact__icon contact__icon--square"></span>
        /simplyshinebyr
      </li>
    </ul>
  </div>
</section>

</body>
</html>
```